Flyer for Lawnmowing and gardening business

We are a lawn mowing and gardening business needing a flyer designed listing our services and business info.
The flyer should include all business information and contact details as below.

Lawn mowing
Gardening
Green waste removal
Pruning
Weeding
Vegetable Garden Creation

Phone number:0481657240

As well as the logo provided

Target Market(s)

Local people wanting someone to care for their garden.

Industry/Entity Type

Gardener

Font styles to use
Serif

Requirements
Must have
• Business Logo
• All business info and services provided. EG
• Lawn mowing
• Gardening
• Green waste removal
• Pruning
• Weeding
• Vegetable Garden Creation
• Phone number:0481657240
Nice to have
• Earthy tones, clean and simple flyer design

```html
<!DOCTYPE html>
<html lang="en">
<head>
<meta charset="utf-8">
<title>Fernleigh Yard – Lawn Mowing &amp; Gardening Flyer</title>
<link rel="stylesheet" href="https://fonts.googleapis.com/css2?family=Quicksand:wght@700&family=Playfair+Display:ital@1&display=swap">
<style>
  :root {
    --night: #0b111b;
    --night-soft: #141c29;
    --stitch: #e9ecef;
    --paper: #ffffff;
    --brand-green: #2f6b2a;
    --service-grey: #8d979b;
    --service-edge: #c5cbcd;
    --highlight: #f4f4f0;
    --leaf-light: #cbbfa6;
    --leaf-mid: #8a7a60;
    --leaf-dark: #3a3128;
  }
  * { margin: 0; padding: 0; box-sizing: border-box; }
  html, body { width: 900px; height: 1200px; overflow: hidden; background: var(--night); }
  .flyer {
    position: relative;
    width: 900px;
    height: 1200px;
    overflow: hidden;
    background: radial-gradient(ellipse at 50% 45%, var(--night-soft) 0%, var(--night) 70%);
    font-family: "Quicksand", "Arial Rounded MT Bold", sans-serif;
  }
  .header-frame {
    position: absolute;
    left: 90px;
    top: -40px;
    width: 705px;
    height: 250px;
    border: 3px dashed var(--stitch);
    border-radius: 40px;
  }
  .brand-card {
    position: absolute;
    left: 255px;
    top: 45px;
    width: 375px;
    height: 135px;
    background: var(--paper);
    display: flex;
    align-items: center;
    justify-content: center;
    gap: 16px;
  }
  .brand-mark {
    width: 26px;
    height: 26px;
    border-radius: 50%;
    background: var(--brand-green);
  }
  .brand-name {
    font-family: "Quicksand", sans-serif;
    font-weight: 700;
    font-size: 38px;
    color: var(--brand-green);
  }
  .leaf-feature {
    position: absolute;
    left: 240px;
    top: 200px;
    width: 480px;
    height: 790px;
    border-radius: 45% 55% 40% 60%;
    background: radial-gradient(ellipse at 45% 50%, var(--leaf-light) 0%, var(--leaf-mid) 35%, var(--leaf-dark) 60%, rgba(11,17,27,0) 78%);
    opacity: 0.85;
  }
  .services {
    position: absolute;
    left: 0;
    top: 630px;
    width: 900px;
    list-style: none;
    text-align: center;
  }
  .services li {
    font-size: 34px;
    line-height: 48px;
    letter-spacing: 6px;
    text-transform: uppercase;
    color: var(--service-grey);
    -webkit-text-stroke: 1px var(--service-edge);
  }
  .services .service-highlight {
    margin-top: 2px;
    font-size: 36px;
    letter-spacing: 4px;
    color: var(--highlight);
    -webkit-text-stroke: 0;
  }
  .contact {
    position: absolute;
    left: 0;
    top: 945px;
    width: 900px;
    text-align: center;
    color: var(--highlight);
  }
  .contact-label {
    font-family: "Playfair Display", Georgia, serif;
    font-style: italic;
    font-size: 36px;
    letter-spacing: 3px;
  }
  .contact-number {
    margin-top: 4px;
    font-size: 40px;
    letter-spacing: 8px;
  }
</style>
</head>
<body>
  <main class="flyer">
    <div class="leaf-feature" role="img" aria-label="Photograph of a dried autumn leaf against a dark background"></div>

    <header class="header-frame"></header>
    <div class="brand-card">
      <span class="brand-mark"></span>
      <span class="brand-name">Fernleigh Yard</span>
    </div>

    <ul class="services">
      <li>Lawn Mowing</li>
      <li>Gardening</li>
      <li>Green Waste Removal</li>
      <li>Pruning</li>
      <li>Weeding</li>
      <li class="service-highlight">Vegetable Garden Creation</li>
    </ul>

    <section class="contact">
      <p class="contact-label">Phone number:</p>
      <p class="contact-number">0481657240</p>
    </section>
  </main>
</body>
</html>
```